New label design for Vitmain Water beverage

This is to create a new label for a vitamin water company called Zelbo Vitamin. The label should be in dual languages. English and Arabic as seen attached for a previous example. You do not have to create an Arabic logo, just make space for it and I will have someon else do it. If you think you can do it, go ahead. I have also attached the bottle dimensions we are thinking of using. Please provide a new bottle design if you see fit. Please remember the bottle size is 400ml, and no pressure If I don't get a great bottle design, then I will use the attached one in that case. Please make the label diverse for various flavors, so it would apply easily and color print friendly. The brand is healthy, sporty, low or no sugars, no artificial flavors and no artificial coloring. All vitamins, minirals and electrolytes are healthy and real. Three flavors: pomogranite cherry, tropical citrus, and kiwi strawberry. So, each label would have different vitamins and offers unique components. Make it hip, trendy yet classy.
Good Luck!!!
Updates

Target Market(s)

Age 15-40 males and females

Industry/Entity Type

Water Company

Requirements
Nice to have
• Plastic PET bottle design
• a 500 ml version

```html
<!DOCTYPE html>
<html lang="en">
<head>
<meta charset="utf-8">
<title>Zelbo Vitamin – Label Flavours</title>
<link href="https://fonts.googleapis.com/css2?family=Marcellus&family=Sue+Ellen+Francisco&display=swap" rel="stylesheet">
<style>
  :root {
    --stage-bg: #e6ebf2;
    --stage-glow: #ffffff;
    --citrus: #0bbdf0;
    --citrus-deep: #0a62b4;
    --citrus-light: #6fd3f5;
    --cherry: #ec176a;
    --cherry-deep: #c9114f;
    --cherry-light: #f49bc3;
    --white: #ffffff;
    --divider: #d0d6de;
  }
  * { margin: 0; padding: 0; box-sizing: border-box; }
  html, body { width: 1081px; height: 1200px; overflow: hidden; background: var(--white); }
  .canvas { position: relative; width: 1081px; height: 1200px; overflow: hidden; }

  .stage {
    position: absolute; left: 0; top: 0; width: 1081px; height: 805px;
    background: radial-gradient(ellipse 340px 420px at 490px 390px, var(--stage-glow) 40%, var(--stage-bg) 100%);
  }
  .bottle-render {
    position: absolute; left: 385px; top: 95px; width: 205px; height: 575px;
    border-radius: 60px 60px 18px 18px;
    background: linear-gradient(90deg, #1fa9e6 0%, #5fd0f7 35%, #3cbdf0 65%, #1a9ad8 100%);
  }

  .label {
    position: absolute; top: 805px; width: 533px; height: 390px; overflow: hidden;
  }
  .label--citrus { left: 0; background: var(--citrus); --accent: var(--citrus); }
  .label--cherry { left: 535px; width: 546px; background: var(--cherry); --accent: var(--cherry); }
  .label-divider { position: absolute; left: 533px; top: 805px; width: 2px; height: 395px; background: var(--divider); }

  .label__waves { position: absolute; left: 0; top: 0; width: 100%; height: 100%; }
  .brand-disc {
    position: absolute; left: 33px; top: 28px; width: 136px; height: 136px;
    border-radius: 50%; background: var(--white);
  }
  .brand-name {
    position: absolute; left: 185px; top: 20px;
    font-family: "Marcellus", serif; color: var(--white); font-weight: 400;
    line-height: 1;
  }
  .brand-name__main { display: block; font-size: 100px; letter-spacing: 6px; }
  .brand-name__sub { display: block; font-size: 54px; letter-spacing: 22px; margin-top: 4px; text-transform: lowercase; }

  .hand { font-family: "Sue Ellen Francisco", cursive; position: absolute; }
  .volume { left: 445px; top: 203px; font-size: 26px; color: var(--white); }
  .flavour { left: 45px; top: 270px; font-size: 40px; letter-spacing: 3px; color: var(--accent); transform: rotate(7deg); transform-origin: left center; white-space: nowrap; }
  .vitamins { left: 332px; top: 340px; font-size: 20px; letter-spacing: 2px; color: var(--accent); word-spacing: 10px; }
  .label--cherry .vitamins { left: 335px; }
</style>
</head>
<body>
<div class="canvas">
  <section class="stage">
    <div class="bottle-render" role="img" aria-label="400 ml PET bottle of Zelbo Vitamin tropical citrus with wrap-around label"></div>
  </section>

  <section class="label label--citrus">
    <svg class="label__waves" viewBox="0 0 533 390" preserveAspectRatio="none">
      <defs>
        <linearGradient id="citrusBand" x1="0" x2="1">
          <stop offset="0" stop-color="#0a62b4"/>
          <stop offset="0.35" stop-color="#58c6ee"/>
          <stop offset="1" stop-color="#0a55a8"/>
        </linearGradient>
      </defs>
      <path d="M0 255 C150 190 330 195 533 240 L533 300 C330 255 150 250 0 300 Z" fill="url(#citrusBand)"/>
      <path d="M0 278 C150 245 330 250 533 285 L533 390 L0 390 Z" fill="#ffffff"/>
      <path d="M0 268 C150 238 330 242 533 272" fill="none" stroke="#bfe9f8" stroke-width="3"/>
    </svg>
    <div class="brand-disc"></div>
    <div class="brand-name"><span class="brand-name__main">ZELBO</span><span class="brand-name__sub">Vitamin</span></div>
    <div class="hand volume">400 ml</div>
    <div class="hand flavour">tropical citrus</div>
    <div class="hand vitamins">vitamins: B2, B1, C</div>
  </section>

  <div class="label-divider"></div>

  <section class="label label--cherry">
    <svg class="label__waves" viewBox="0 0 546 390" preserveAspectRatio="none">
      <defs>
        <linearGradient id="cherryBand" x1="0" x2="1">
          <stop offset="0" stop-color="#f8a5c8"/>
          <stop offset="0.4" stop-color="#e6345f"/>
          <stop offset="1" stop-color="#f49bc3"/>
        </linearGradient>
      </defs>
      <path d="M0 250 C150 195 340 195 546 240 L546 300 C340 255 150 250 0 295 Z" fill="url(#cherryBand)"/>
      <path d="M0 275 C150 245 340 250 546 285 L546 390 L0 390 Z" fill="#ffffff"/>
      <path d="M0 265 C150 235 340 240 546 272" fill="none" stroke="#f9c6db" stroke-width="3"/>
    </svg>
    <div class="brand-disc"></div>
    <div class="brand-name"><span class="brand-name__main">ZELBO</span><span class="brand-name__sub">Vitamin</span></div>
    <div class="hand volume">400 ml</div>
    <div class="hand flavour">pomogranite cherry</div>
    <div class="hand vitamins">vitamins: B2, B1, C</div>
  </section>
</div>
</body>
</html>
```